Business Cards For A cell Phone Company
Linden Cellular
Business Cards For A cell Phone Company - Retailers
Creative Brief
Simple
Tobias Krell
Operations Manager
2864 Belmore Ave Cincinnati OH 45219
tobias.krell@lindencellular-mail.com
www.lindencellular-mail.com
Concepts
Business Cards/Letterhead/ Envelopes/Notepads/Tshirt/labels for quiet tin crate
Business cards and company letter head for Orchard Noodle Court

```html
<!DOCTYPE html>
<html lang="en">
<head>
<meta charset="utf-8">
<title>Linden Cellular — Business Cards</title>
<link rel="stylesheet" href="https://fonts.googleapis.com/css2?family=Arimo:wght@400;700&display=swap">
<style>
  :root{
    --page:#e6e6e6;
    --card:#ffffff;
    --red:#d4101c;
    --red-dark:#8f0a12;
    --red-light:#e8343c;
    --silver:#c9c9cb;
    --silver-dark:#9a9a9d;
    --ink-light:#ffffff;
  }
  *{margin:0;padding:0;box-sizing:border-box}
  html,body{width:1200px;height:901px;overflow:hidden;background:var(--page)}
  body{font-family:"Arimo",Arial,sans-serif;position:relative}
  .card{
    position:absolute;left:260px;width:680px;height:389px;
    border-radius:26px;overflow:hidden;background:var(--card);
    box-shadow:0 6px 18px rgba(0,0,0,.18);
  }
  .card--back{top:40px}
  .card--front{top:472px}
  .card-bg{position:absolute;inset:0;width:100%;height:100%}
  .brand{
    position:absolute;display:flex;align-items:center;gap:14px;
    left:0;right:0;justify-content:center;
  }
  .brand-mark{width:34px;height:34px;background:var(--red)}
  .brand-name{
    font-weight:700;font-size:38px;color:var(--red);
    letter-spacing:1px;text-transform:uppercase;
  }
  .card--back .brand{top:205px}
  .card--front .brand{top:78px}
  .back-web{
    position:absolute;left:70px;top:42px;color:var(--ink-light);
    font-size:13px;letter-spacing:.5px;
  }
  .holder{position:absolute;left:30px;top:228px;color:var(--ink-light)}
  .holder-name{font-size:22px;font-weight:400}
  .holder-title{font-size:15px;margin-top:4px}
  .contacts{
    position:absolute;left:400px;top:250px;list-style:none;color:var(--ink-light);
    font-size:12.5px;line-height:17px;
  }
  .contacts li{display:flex;align-items:flex-start;gap:8px}
  .contacts .icon{width:13px;height:13px;flex:none;margin-top:2px}
  .contacts .indent{padding-left:21px}
</style>
</head>
<body>

<!-- Card back -->
<section class="card card--back" aria-label="Business card back">
  <svg class="card-bg" viewBox="0 0 680 389" preserveAspectRatio="none">
    <defs>
      <linearGradient id="backRed" x1="0" y1="0" x2="1" y2="1">
        <stop offset="0" stop-color="var(--red-light)"/>
        <stop offset="1" stop-color="var(--red-dark)"/>
      </linearGradient>
    </defs>
    <path d="M0,0 H680 V70 C520,78 300,110 0,168 Z" fill="var(--silver)"/>
    <path d="M0,0 H680 V58 C520,64 300,96 0,152 Z" fill="url(#backRed)"/>
  </svg>
  <p class="back-web">www.lindencellular-mail.com</p>
  <div class="brand">
    <span class="brand-mark"></span>
    <span class="brand-name">Linden Cellular</span>
  </div>
</section>

<!-- Card front -->
<section class="card card--front" aria-label="Business card front">
  <svg class="card-bg" viewBox="0 0 680 389" preserveAspectRatio="none">
    <defs>
      <radialGradient id="frontRed" cx=".5" cy=".35" r=".8">
        <stop offset="0" stop-color="var(--red-light)"/>
        <stop offset=".6" stop-color="var(--red)"/>
        <stop offset="1" stop-color="var(--red-dark)"/>
      </radialGradient>
      <linearGradient id="silverBand" x1="0" y1="0" x2="1" y2="0">
        <stop offset="0" stop-color="var(--silver)"/>
        <stop offset=".5" stop-color="#ececed"/>
        <stop offset="1" stop-color="var(--silver-dark)"/>
      </linearGradient>
    </defs>
    <path d="M0,200 H58 L72,184 L86,200 C300,200 500,210 680,236 V389 H0 Z" fill="url(#silverBand)"/>
    <path d="M0,208 H58 L72,192 L86,208 C300,208 500,218 680,244 V389 H0 Z" fill="url(#frontRed)"/>
  </svg>

  <div class="brand">
    <span class="brand-mark"></span>
    <span class="brand-name">Linden Cellular</span>
  </div>

  <div class="holder">
    <p class="holder-name">Tobias Krell</p>
    <p class="holder-title">Owner / C.E.O</p>
  </div>

  <ul class="contacts">
    <li>
      <svg class="icon" viewBox="0 0 14 14"><circle cx="7" cy="7" r="7" fill="#fff"/><path d="M7,3 a2.5,2.5 0 0 1 2.5,2.5 C9.5,7.5 7,11 7,11 S4.5,7.5 4.5,5.5 A2.5,2.5 0 0 1 7,3Z" fill="var(--red)"/></svg>
      <span>2864 Belmore Ave,</span>
    </li>
    <li class="indent">Cincinnati OH 45219</li>
    <li>
      <svg class="icon" viewBox="0 0 14 14"><circle cx="7" cy="7" r="7" fill="#fff"/><rect x="5" y="3" width="4" height="8" rx="1" fill="var(--red)"/></svg>
      <span>513-555-0142</span>
    </li>
    <li>
      <svg class="icon" viewBox="0 0 14 14"><circle cx="7" cy="7" r="7" fill="#fff"/><rect x="5" y="3" width="4" height="8" rx="1" fill="var(--red)"/></svg>
      <span>513-555-0178</span>
    </li>
    <li>
      <svg class="icon" viewBox="0 0 14 14"><circle cx="7" cy="7" r="7" fill="#fff"/><rect x="5" y="3" width="4" height="8" rx="1" fill="var(--red)"/></svg>
      <span>513-555-0193</span>
    </li>
    <li>
      <svg class="icon" viewBox="0 0 14 14"><circle cx="7" cy="7" r="7" fill="#fff"/><rect x="3.5" y="4.5" width="7" height="5" fill="var(--red)"/><path d="M3.5,4.5 L7,7.5 L10.5,4.5" stroke="#fff" stroke-width=".8" fill="none"/></svg>
      <span>tobias.krell@lindencellular-mail.com</span>
    </li>
    <li>
      <svg class="icon" viewBox="0 0 14 14"><circle cx="7" cy="7" r="7" fill="#fff"/><circle cx="7" cy="7" r="3.6" fill="none" stroke="var(--red)" stroke-width="1"/><path d="M3.4,7 H10.6 M7,3.4 V10.6" stroke="var(--red)" stroke-width=".8"/></svg>
      <span>www.lindencellular-mail.com</span>
    </li>
  </ul>
</section>

</body>
</html>
```